Redesign our current website with a more professional feel

We currently have a running website that generates some traffic and looks ok but now we want to revamp it with professional eye catching design.
We are open to proposals and open to any new ideas or suggestions but we have to see your previous work.
our current site is www.brelk-solutions.com.au

Thank you for your time and we look forward to seeing your proposals

Target Market(s)

Business owners, managers

Industry/Entity Type

Security

Number of Pages Required

5+ page

```html
<!DOCTYPE html>
<html lang="en">
<head>
<meta charset="utf-8">
<title>Brelk Solutions – Security Services</title>
<link href="https://fonts.googleapis.com/css2?family=Crimson+Text:wght@400;600&family=Lato:ital,wght@0,400;0,700;1,400&display=swap" rel="stylesheet">
<style>
:root{
  --brand:#1d3e8e;
  --brand-soft:#6f84d8;
  --ink:#333;
  --muted:#555;
  --band:#000;
  --panel:#efefef;
  --rule:#d6d6d6;
  --footer:#333333;
  --footer-box:#3d3d3d;
  --footer-line:#5a5a5a;
  --white:#fff;
}
*{margin:0;padding:0;box-sizing:border-box}
html,body{width:913px;height:1200px;overflow:hidden;background:var(--white)}
body{font-family:"Lato",sans-serif;color:var(--ink)}
.page{position:relative;width:913px;height:1200px;overflow:hidden}
.serif{font-family:"Crimson Text",serif}

/* header */
.site-header{position:absolute;left:0;top:0;width:913px;height:92px;border-top:2px solid var(--brand-soft);background:linear-gradient(#fff,#f1f1f1)}
.brand{position:absolute;left:110px;top:28px;display:flex;align-items:center;gap:8px}
.brand-dot{width:14px;height:14px;border-radius:50%;background:var(--brand)}
.brand-name{font-family:"Crimson Text",serif;font-weight:600;font-size:26px;color:var(--brand);letter-spacing:1px}
.call{position:absolute;right:108px;top:11px;display:flex;gap:6px;align-items:center}
.call-text{font-style:italic;color:#333;line-height:1.1}
.call-text small{display:block;font-size:9.5px}
.call-text strong{font-weight:400;font-size:16px}
.main-nav{position:absolute;right:105px;top:70px;display:flex;align-items:center;font-family:"Crimson Text",serif;font-size:13px;letter-spacing:.3px}
.main-nav a{color:#222;text-decoration:none;padding:0 7px;border-left:1px solid #bbb;line-height:15px}
.main-nav a.home{border:0;padding-right:12px}

/* hero */
.hero{position:absolute;left:0;top:92px;width:913px;height:296px;background:linear-gradient(180deg,#b9c2c9 0%,#8e9a86 35%,#d9d4c4 60%,#5d7086 100%)}
.hero-arrow{position:absolute;top:156px;width:28px;height:28px;border-radius:50%;background:#111;display:flex;align-items:center;justify-content:center}
.hero-arrow.prev{left:73px}.hero-arrow.next{left:809px}
.tagline{position:absolute;left:0;top:388px;width:913px;height:42px;background:var(--band);color:var(--white);font-size:18.5px;text-align:center;line-height:42px}

/* about */
.about-title{position:absolute;left:0;top:455px;width:913px;text-align:center;font-size:22px;color:var(--brand);font-weight:600}
.about-text{position:absolute;left:112px;top:505px;width:690px;text-align:center;font-size:10.2px;line-height:16px;color:#444}
.btn{position:absolute;left:417px;top:587px;width:79px;height:22px;background:var(--brand);color:#fff;font-size:10px;font-weight:700;text-align:center;line-height:22px;border-radius:2px}

/* services */
.services{position:absolute;left:0;top:642px;width:913px;height:206px;background:var(--panel);border-top:1px solid #ddd;border-bottom:1px solid #ddd}
.services h2{position:absolute;left:0;top:20px;width:913px;text-align:center;font-size:22px;color:var(--brand);font-weight:600}
.service{position:absolute;top:66px;width:126px;text-align:center}
.service svg{display:block;margin:0 auto}
.service-icon{position:absolute;left:48px;top:12px;width:30px;height:30px;border-radius:4px;background:#2b2b2b}
.service p{font-family:"Crimson Text",serif;font-size:14px;line-height:16px;color:#222;margin-top:10px}

/* info columns */
.col{position:absolute;top:872px;width:216px}
.col-head{display:flex;align-items:center;gap:8px;padding-bottom:6px;border-bottom:1px solid var(--rule);font-family:"Crimson Text",serif;font-size:16px;color:var(--brand);font-weight:600}
.news-item{padding:8px 0 7px;border-bottom:1px dashed #ccc;font-size:10px;line-height:14px;color:#333}
.news-item:last-of-type{border:0}
.news-item b{display:block}
.more{display:block;text-align:right;font-size:10px;font-weight:700;color:var(--brand);margin-top:4px}
.quote{margin-top:10px;background:#ececec;border-radius:6px;padding:9px 6px 16px 14px;font-style:italic;font-size:10px;line-height:16px;color:#333}
.quote .mark{font-size:26px;color:#bbb;line-height:0;vertical-align:-8px;margin-right:2px;font-family:"Crimson Text",serif}
.author{display:flex;align-items:center;gap:12px;margin:-14px 0 0 15px}
.avatar{width:50px;height:50px;border-radius:3px;background:linear-gradient(#8a96a3,#3c4654);border:2px solid #fff}
.author span{font-size:10.5px;margin-top:20px}
.testimonial .more{margin-top:0}
.field{margin-top:14px;width:214px;height:21px;border:1px solid #bbb;border-radius:2px;font-size:9px;color:#777;font-style:italic;padding:4px 7px}
.field+.field{margin-top:6px}
.field.msg{height:54px}
.submit{margin-top:12px;width:52px;height:21px;background:var(--brand-soft);color:#fff;font-size:11px;font-weight:700;text-align:center;line-height:21px;border-radius:2px}

/* footer */
.site-footer{position:absolute;left:0;top:1082px;width:913px;height:118px;background:var(--footer);color:#eee}
.fbox{position:absolute;top:15px;height:58px;background:var(--footer-box);border:1px solid var(--footer-line);padding:4px 9px}
.fbox h3{font-family:"Crimson Text",serif;font-weight:400;font-size:13px;margin-bottom:5px}
.fbox.contact{padding:4px 7px}
.sub-input{display:inline-block;width:137px;height:21px;background:#5a5a5a;font-size:10px;font-style:italic;color:#ddd;padding:4px 6px;vertical-align:middle}
.sub-go{display:inline-block;width:24px;height:21px;background:#5a5a5a;margin-left:4px;vertical-align:middle;text-align:center;line-height:21px}
.contact-line{display:flex;align-items:center;gap:7px;font-size:9.5px;line-height:16px;white-space:nowrap}
.contact-line svg{flex:none}
.social{display:flex;gap:12px;margin-top:4px}
.social i{width:18px;height:18px;border-radius:3px;background:#6b7fc4;display:block}
.social i+i{background:#62a9d8}.social i+i+i{background:#e07b2a}
.footer-brand{position:absolute;right:110px;top:33px;display:flex;align-items:center;gap:7px}
.footer-brand .brand-name{color:#cfcfcf;font-size:22px}
.footer-brand .brand-dot{background:#cfcfcf;width:11px;height:11px}
.footer-nav{position:absolute;left:108px;top:94px;font-size:11px;color:#eee}
.footer-nav span{margin:0 4px;color:#aaa}
.copy{position:absolute;right:108px;top:93px;font-size:11px;color:#eee}
</style>
</head>
<body>
<div class="page">

<header class="site-header">
  <div class="brand"><span class="brand-dot"></span><span class="brand-name">BRELK SOLUTIONS</span></div>
  <div class="call">
    <svg width="26" height="26" viewBox="0 0 26 26"><circle cx="13" cy="13" r="11" fill="none" stroke="#1d3e8e" stroke-width="1.5"/><path d="M9 7c-2 2 0 8 5 12 2 1 3 0 3-1l-2-2-2 1c-2-1-3-3-4-5l1-2-1-3z" fill="#1d3e8e"/></svg>
    <div class="call-text"><small>Call Us Today</small><strong>1300 42 8190</strong></div>
  </div>
  <nav class="main-nav">
    <a class="home" href="#" aria-label="Home"><svg width="14" height="13" viewBox="0 0 14 13"><path d="M7 0L0 6h2v7h4V9h2v4h4V6h2z" fill="#1d3e8e"/></svg></a>
    <a href="#">ABOUT US</a><a href="#">SERVICES</a><a href="#">NEWS</a><a href="#">SPECIAL OFFERS</a><a href="#">CONTACT US</a>
  </nav>
</header>

<section class="hero" role="img" aria-label="Aerial photograph of a harbour city with a waterfront opera house">
  <span class="hero-arrow prev"><svg width="10" height="14"><path d="M8 1L2 7l6 6" stroke="#fff" fill="none" stroke-width="1.5"/></svg></span>
  <span class="hero-arrow next"><svg width="10" height="14"><path d="M2 1l6 6-6 6" stroke="#fff" fill="none" stroke-width="1.5"/></svg></span>
</section>
<div class="tagline serif">Our Focus And Goal Is To Provide The&nbsp; Best Possible Security Service To Our Customer’s</div>

<section class="about">
  <h1 class="about-title serif">ABOUT BRELK SOLUTIONS</h1>
  <p class="about-text">Lorem ipsum dolor sit amet, consectetuer adipiscing elit,Sed diam nonummy nibh euismod tincidunt ut laoreet dolore magna aliquam erat volutpat. Ut wisi enim ad minim veniam, quis nostrud exerci tation ullamcorper suscipit lobortis nisl ut aliquip&nbsp; commodo consequat. Duis autem vel eum iriure dolor in hendrerit in vulputate velit esse molestie consequat, vel ill dolore eu feugiat nulla facilisis at vero eros et accumsan et iusto odio dignissim qui blandit praesent luptatumdeelenit augue duis dolore te feugait nulla facilisi.</p>
  <div class="btn">READ MORE</div>
</section>

<section class="services">
  <h2 class="serif">OUR SERVICES</h2>
  <div class="service" style="left:106px"><svg width="126" height="66"><ellipse cx="63" cy="33" rx="60" ry="30" fill="none" stroke="#6f84d8" stroke-width="4"/></svg><span class="service-icon" role="img" aria-label="Concierge desk icon"></span><p>Concierge<br>Services</p></div>
  <div class="service" style="left:249px"><svg width="126" height="66"><ellipse cx="63" cy="33" rx="60" ry="30" fill="none" stroke="#6f84d8" stroke-width="4"/></svg><span class="service-icon" role="img" aria-label="Control room monitor icon"></span><p>Control<br>Room</p></div>
  <div class="service" style="left:393px"><svg width="126" height="66"><ellipse cx="63" cy="33" rx="60" ry="30" fill="none" stroke="#6f84d8" stroke-width="4"/></svg><span class="service-icon" role="img" aria-label="Security guard icon"></span><p>Static<br>Guarding</p></div>
  <div class="service" style="left:536px"><svg width="126" height="66"><ellipse cx="63" cy="33" rx="60" ry="30" fill="none" stroke="#6f84d8" stroke-width="4"/></svg><span class="service-icon" role="img" aria-label="Patrol car icon"></span><p>Mobile<br>Patrols</p></div>
  <div class="service" style="left:680px"><svg width="126" height="66"><ellipse cx="63" cy="33" rx="60" ry="30" fill="none" stroke="#6f84d8" stroke-width="4"/></svg><span class="service-icon" role="img" aria-label="Security camera icon"></span><p>CCTV &amp; Alarm<br>Installations</p></div>
</section>

<section class="col" style="left:107px">
  <div class="col-head"><svg width="18" height="14"><path d="M1 5h4l9-4v12L5 9H1z" fill="#222"/></svg>LATEST NEWS</div>
  <div class="news-item"><b>06/01/2016</b>Lorem ipsum dolor sit amet, cctetuer ipiscingin elit, sed diam nummy nibh eui smod tinciduntiot vulputate velit esse molestie</div>
  <div class="news-item"><b>07/01/2016</b>Lorem ipsum dolor sit amet, cctetuer dipiscingin elit, sed diam nummy nibh eui smod tinciduntiot vulputate velit esse molestie</div>
  <span class="more">Read more »</span>
</section>

<section class="col testimonial" style="left:349px">
  <div class="col-head"><svg width="18" height="15"><path d="M1 1h11v7H5l-3 3V8H1z" fill="#222"/><path d="M13 4h4v7h-1v3l-3-3H7V9h6z" fill="#222"/></svg>CLIENT TESTIMONIALS</div>
  <div class="quote"><span class="mark">“</span>Duis autem vel eum iriureol hder in vultat velit esse moles conqat vela ilu dolor ugiat.Duis autem vel eum ure hendrern vultat velit esse autm vel eum iriure dol</div>
  <div class="author"><span class="avatar" role="img" aria-label="Client portrait"></span><span>Mr. Dolore Eu Feugiat</span></div>
  <span class="more">Read more »</span>
</section>

<section class="col" style="left:591px">
  <div class="col-head"><svg width="18" height="16"><path d="M2 2h9v3M2 2v13h9v-3" stroke="#222" fill="none" stroke-width="1.6"/><path d="M8 11l7-7 2 2-7 7H8z" fill="#222"/></svg>QUICK CONTACT</div>
  <div class="field">Name</div>
  <div class="field">Email</div>
  <div class="field msg">Message</div>
  <div class="submit">Submit</div>
</section>

<footer class="site-footer">
  <div class="fbox" style="left:107px;width:187px"><h3>Subscribe to Newsletter</h3><span class="sub-input">Email here</span><span class="sub-go"><svg width="8" height="10"><path d="M1 1l5 4-5 4" stroke="#fff" stroke-width="2" fill="none"/></svg></span></div>
  <div class="fbox contact" style="left:311px;width:158px"><h3>Contact Us</h3>
    <div class="contact-line"><svg width="9" height="9"><path d="M1 1c0 4 3 7 7 7l1-2-2-1-1 1C4 5 4 4 3 3l1-1-1-2z" fill="#ddd"/></svg>1300 42 8190</div>
    <div class="contact-line"><svg width="9" height="7"><rect x=".5" y=".5" width="8" height="6" fill="none" stroke="#ddd"/><path d="M.5.5l4 3 4-3" stroke="#ddd" fill="none"/></svg>info@brelk-solutions.com.au</div>
  </div>
  <div class="fbox" style="left:480px;width:91px"><h3>Follow Us</h3><div class="social"><i></i><i></i><i></i></div></div>
  <div class="footer-brand"><span class="brand-dot"></span><span class="brand-name">BRELK</span></div>
  <nav class="footer-nav">Home<span>|</span>About Us<span>|</span>Services<span>|</span>News<span>|</span>Special Offers<span>|</span>Contact Us</nav>
  <div class="copy">© 2016&nbsp; Brelk Solutions. All Rights Reserved</div>
</footer>

</div>
</body>
</html>
```